Stunning Podcast Cover Design for The Morning Harbor Hour!!

I need a design for my new podcast.
I will need it in a variety of size/formats, such as a large version for my podcast website homepage, the thumbnail for Tunewell, Pondcast, Vexa Stream and more.

The podcast is called "The Morning Harbor Hour" and it includes topics such as: business, entrepreneurship, finance, budgeting, estate planning, end-of-life planning, travel, business and personal stories featuring people from all over the world, life in general, and more.

I don't have a vision in mind so am looking for creativity but it definitely needs to have the colour gold in it somewhere! No cartoon characters please.

I will provide comments/feedback to each designer.

***UPDATE: Please see some photos of me that can be used in the podcast design.

Here is some tips on creating podcast designs. https://www.castleafy.example/blog/10-tips-create-awesome-podcast-artwork

Target Market(s)

Adults 25 - 65

Font styles to use
Other font styles liked:
• something modern - see my company logo as an example

Colors

Designer to choose colors to be used in the design.

Requirements
Must have
• The colour gold in it
Nice to have
• I feel like the word "The" should be smaller then the other three words.
• I would like to see designs with a white coloured background and a black coloured one also...
• Perhaps designs with a filter over the photo, and without.
• Perhaps use my photo, or don't use my photo!
• Please see some photos of me that can be used in the podcast design.
• Here is some tips on creating podcast designs. https://www.castleafy.example/blog/10-tips-create-awesome-podcast-artwork
Should not have
• cartoon characters
• Corny 1990's "Evenings Among the Gilded and Glamorous" look - see https://www.vidorama.example/watch?v=Q7T2KX8PLBZ

```html
<!DOCTYPE html>
<html lang="en">
<head>
<meta charset="utf-8">
<title>The Morning Harbor Hour – Cover Options</title>
<link rel="stylesheet" href="https://fonts.googleapis.com/css2?family=Jost:wght@500;600&display=swap">
<style>
  :root {
    --page-bg: #ffffff;
    --gold-light: #f7e68a;
    --gold-mid: #e2bf4a;
    --gold-deep: #b8861f;
    --wall-gold-1: #e6c67f;
    --wall-gold-2: #d9b56a;
    --wall-grey-1: #b9bfca;
    --wall-grey-2: #8e96a3;
    --window-dark: #2c3138;
    --window-gold: #caa456;
    --portrait-dark: #1d2128;
    --portrait-hair: #5a3a28;
    --portrait-gold: #3a3026;
  }
  * { margin: 0; padding: 0; box-sizing: border-box; }
  html, body {
    width: 1200px; height: 1200px; overflow: hidden;
    background: var(--page-bg);
  }
  .canvas { position: relative; width: 1200px; height: 1200px; }

  .cover {
    position: absolute; top: 320px;
    width: 560px; height: 560px; overflow: hidden;
  }
  .cover--gold { left: 20px; }
  .cover--natural { left: 620px; }

  .cover__photo { position: absolute; inset: 0; }
  .cover__photo span { position: absolute; display: block; }
  .photo__wall { inset: 0; }
  .photo__window { top: 0; right: 0; width: 180px; height: 280px; }
  .photo__portrait {
    left: 340px; top: 88px; width: 220px; height: 472px;
    border-radius: 100px 100px 0 0;
  }

  .cover--gold .photo__wall { background: linear-gradient(100deg, var(--wall-gold-1), var(--wall-gold-2)); }
  .cover--gold .photo__window { background: linear-gradient(180deg, #efd48f, var(--window-gold)); }
  .cover--gold .photo__portrait { background: linear-gradient(180deg, var(--portrait-gold) 0%, var(--portrait-hair) 35%, var(--portrait-dark) 75%); }

  .cover--natural .photo__wall { background: linear-gradient(100deg, var(--wall-grey-2) 0%, var(--wall-grey-1) 35%, #a6adb9 100%); }
  .cover--natural .photo__window { background: linear-gradient(180deg, #9cc4e6 0%, var(--window-dark) 25%, #a35a3a 30%, var(--window-dark) 45%); }
  .cover--natural .photo__portrait { background: linear-gradient(180deg, var(--portrait-hair) 0%, #6b4530 35%, var(--portrait-dark) 75%); }

  .cover__title {
    position: absolute; left: 20px; top: 0;
    font-family: "Jost", "Futura", sans-serif;
    font-weight: 600; line-height: 1;
    text-transform: uppercase;
  }
  .title__line {
    position: absolute; left: 0; white-space: nowrap;
    background: linear-gradient(180deg, var(--gold-light) 0%, var(--gold-mid) 55%, var(--gold-deep) 100%);
    -webkit-background-clip: text; background-clip: text;
    color: transparent;
  }
  .title__line--small { font-size: 40px; letter-spacing: -0.5px; }
  .title__line--large { font-size: 60px; letter-spacing: -1px; font-weight: 500; }
  .title__the { top: 150px; }
  .title__morning { top: 200px; }
  .title__harbor { top: 272px; }
  .title__hour { top: 352px; }
</style>
</head>
<body>
<main class="canvas">

  <section class="cover cover--gold" aria-label="Cover option with gold photo filter">
    <div class="cover__photo" role="img" aria-label="Portrait photo of the host smiling beside a brick wall, tinted gold">
      <span class="photo__wall"></span>
      <span class="photo__window"></span>
      <span class="photo__portrait"></span>
    </div>
    <h1 class="cover__title">
      <span class="title__line title__line--small title__the">The</span>
      <span class="title__line title__line--large title__morning">Morning</span>
      <span class="title__line title__line--large title__harbor">Harbor</span>
      <span class="title__line title__line--small title__hour">Hour</span>
    </h1>
  </section>

  <section class="cover cover--natural" aria-label="Cover option with natural photo">
    <div class="cover__photo" role="img" aria-label="Portrait photo of the host smiling beside a grey painted brick wall">
      <span class="photo__wall"></span>
      <span class="photo__window"></span>
      <span class="photo__portrait"></span>
    </div>
    <h2 class="cover__title">
      <span class="title__line title__line--small title__the">The</span>
      <span class="title__line title__line--large title__morning">Morning</span>
      <span class="title__line title__line--large title__harbor">Harbor</span>
      <span class="title__line title__line--small title__hour">Hour</span>
    </h2>
  </section>

</main>
</body>
</html>
```